Web Developer Needs a Business Card Design

I need a personal business card design that represents me as a web developer for potential employers. I would like the background to be a dark color on the front for contrast with my logo and name. The back will have all my information along with a smaller version of the logo. I want something with a modern look and feel, not too conservative. This will be used for potential employers and freelance work.

Industry/Entity Type

Business

Contact Information for Business Card

Front should have my logo and name. The back should have all my personal information which would include: name: Tom Brevardi, phone: 570-614-9083, email: tombrevardi@mailwisp.com, website url: www.tombrevardi.com, logo, web developer.

Font styles to use
Sans Serif

Requirements
Must have
• Must include my logo. The color palette base color will be the logo color.

```html
<!DOCTYPE html>
<html lang="en">
<head>
<meta charset="utf-8">
<title>Tom Brevardi – Business Card</title>
<link rel="stylesheet" href="https://fonts.googleapis.com/css2?family=Source+Sans+3:wght@400;600&display=swap">
<style>
  :root {
    --backdrop: #1b1b1c;
    --card: #0c0c0d;
    --card-edge: #2a2a2c;
    --teal: #86cfbf;
    --teal-deep: #6fb9a9;
    --ink: #f2f2f2;
    --muted: #cfcfcf;
  }
  * { margin: 0; padding: 0; box-sizing: border-box; }
  html, body {
    width: 1200px; height: 864px; overflow: hidden;
    background: var(--backdrop);
    font-family: "Source Sans 3", "Myriad Pro", Arial, sans-serif;
  }
  .stage {
    width: 1200px; height: 864px;
    display: flex; align-items: center; justify-content: center; gap: 60px;
  }
  .card {
    position: relative;
    width: 500px; height: 286px;
    background: linear-gradient(160deg, #19191b 0%, var(--card) 55%, #050505 100%);
    border: 1px solid var(--card-edge);
    overflow: hidden;
  }

  /* Contact side */
  .card-contact .logo-ring {
    position: absolute; top: 22px; right: 30px;
    width: 74px; height: 74px;
  }
  .identity { position: absolute; left: 26px; top: 108px; }
  .identity .name {
    color: var(--teal); font-size: 22px; font-weight: 400; line-height: 1;
  }
  .identity .role {
    color: var(--ink); font-size: 12.5px; margin-top: 5px;
  }
  .divider {
    position: absolute; left: 26px; right: 30px; top: 160px;
    height: 1px; background: var(--teal-deep);
  }
  .contact-list {
    position: absolute; left: 26px; top: 170px;
    list-style: none;
  }
  .contact-list li {
    display: flex; align-items: center; gap: 8px;
    color: var(--ink); font-size: 13px; line-height: 1; height: 17px;
  }
  .contact-list svg { width: 12px; height: 12px; flex: none; }
  .base-band {
    position: absolute; left: 0; right: 0; bottom: 0; height: 26px;
    background: linear-gradient(90deg, var(--teal-deep), var(--teal) 60%, #a6ddd1);
  }

  /* Front side */
  .card-front {
    display: flex; flex-direction: column; align-items: center; justify-content: center; gap: 14px;
  }
  .card-front .logo-ring { width: 62px; height: 62px; }
  .card-front .wordmark {
    color: var(--ink); font-size: 21px; font-weight: 400; letter-spacing: 0.04em;
  }
</style>
</head>
<body>
<main class="stage">

  <section class="card card-contact" aria-label="Business card, contact side">
    <svg class="logo-ring" viewBox="0 0 74 74" aria-hidden="true">
      <circle cx="37" cy="37" r="33" fill="none" stroke="var(--teal)" stroke-width="5"/>
    </svg>

    <div class="identity">
      <p class="name">Tom Brevardi</p>
      <p class="role">Web Developer</p>
    </div>

    <div class="divider"></div>

    <ul class="contact-list">
      <li>
        <svg viewBox="0 0 12 12" aria-hidden="true">
          <rect width="12" height="12" rx="2.5" fill="var(--teal)"/>
          <path d="M3.6 2.6l1.3 1.6-.7.9c.5 1 1.3 1.8 2.3 2.3l.9-.7 1.6 1.3-.8 1.3C5.6 9.2 2.8 6.4 2.4 3.4z" fill="var(--card)"/>
        </svg>
        <span>570-614-9083</span>
      </li>
      <li>
        <svg viewBox="0 0 12 12" aria-hidden="true">
          <rect width="12" height="12" rx="2.5" fill="var(--teal)"/>
          <rect x="2.5" y="3.5" width="7" height="5" fill="var(--card)"/>
          <path d="M2.5 3.5L6 6.4 9.5 3.5" fill="none" stroke="var(--teal)" stroke-width=".8"/>
        </svg>
        <span>tombrevardi@mailwisp.com</span>
      </li>
      <li>
        <svg viewBox="0 0 12 12" aria-hidden="true">
          <rect width="12" height="12" rx="2.5" fill="var(--teal)"/>
          <circle cx="6" cy="6" r="3.6" fill="none" stroke="var(--card)" stroke-width=".9"/>
          <ellipse cx="6" cy="6" rx="1.5" ry="3.6" fill="none" stroke="var(--card)" stroke-width=".8"/>
          <path d="M2.4 6h7.2" stroke="var(--card)" stroke-width=".8"/>
        </svg>
        <span>www.tombrevardi.com</span>
      </li>
    </ul>

    <div class="base-band"></div>
  </section>

  <section class="card card-front" aria-label="Business card, front side">
    <svg class="logo-ring" viewBox="0 0 62 62" aria-hidden="true">
      <circle cx="31" cy="31" r="27" fill="none" stroke="var(--teal)" stroke-width="4.5"/>
    </svg>
    <p class="wordmark">TOM BREVARDI</p>
  </section>

</main>
</body>
</html>
```